Personal Motivational Quote Poster Design

I would like to create a poster with some of my favorite quotes to hang in my office. I did similar projects in 2012 and 2014. I've uploaded the winning designs so you can get a better idea of what I'm looking for. I will provide feedback on your design within 24 hours of receiving it.

The poster must contain the following quotes:

“What the pupil must learn, if he learns anything at all, is that the world will do most of the work for you, provided you cooperate with it by identifying how it really works and aligning with those realities. If we do not let the world teach us, it teaches us a lesson.” - Harold Wexbury

“I tackle every big new problem by asking two questions: Who has dealt with this problem well? And what can we learn from them?” - Tom Harlow

“If we can really understand the problem, the answer will come out of it, because the answer is not separate from the problem.” - Ravindra Pallathuri

“Success is nothing more than a few simple disciplines, practiced every day; while failure is simply a few errors in judgment, repeated every day. It is the accumulative weight of our disciplines and our judgments that leads us to either fortune or failure.” - Ned Pilsk

“Inaction breeds doubt and fear. Action breeds confidence and courage.” - Walt Brimsley

“What’s the one thing you can do, such that by doing it, everything else will be easier or unnecessary?” - Lenny Druse

Requirements
Must have
• The poster will be 24" high x 36" long and printed on canvas, so the image you create needs to have a resolution of at least 2700 x 3900.
Nice to have
• I don't have an exact vision for how the poster should look, so I am totally open to you using your creativity to develop, arrange and present the content as you'd like.

That said, I would like an image (photo or posterized image) of the person being quoted along with each quote. I do not have specific images that I would like you to use, so you will need to find the images on your own.

The images don't need to be perfect... I am more interested in the poster relating the essence of the quotes and the people being quoted than I am in perfect photographic images of the people being quoted.

```html
<!DOCTYPE html>
<html lang="en">
<head>
<meta charset="utf-8">
<title>Favourite Quotes Poster</title>
<link rel="stylesheet" href="https://fonts.googleapis.com/css2?family=Montserrat:wght@500;700;900&display=swap">
<style>
  :root {
    --backdrop: #b9bab8;
    --frame: #ffffff;
    --panel: #e9e9e6;
    --ink: #2e2e2e;
    --teal-mark: #a6dfe3;  --teal-bar: #45bcc4;  --teal-name: #6b8687;
    --salmon-mark: #f6a68c; --salmon-bar: #f0584a; --salmon-name: #f2664a;
    --mint-mark: #a2dcc2;  --mint-bar: #5cc49a;  --mint-name: #5f7a72;
    --lilac-mark: #b4a4c9; --lilac-bar: #6b4a9a; --lilac-name: #55378a;
    --rose-mark: #f4a7bd;  --rose-bar: #e85b8a;  --rose-name: #ec5a86;
    --photo-light: #d8d8d8; --photo-dark: #3c3c3c;
  }
  * { margin: 0; padding: 0; box-sizing: border-box; }
  html, body { width: 853px; height: 1200px; overflow: hidden; background: var(--backdrop); }
  .poster { position: relative; width: 853px; height: 1200px; overflow: hidden; font-family: "Montserrat", sans-serif; color: var(--ink); }
  .frame { position: absolute; left: 51px; top: 58px; width: 751px; height: 1083px; background: var(--frame); }
  .panel { position: absolute; left: 80px; top: 86px; width: 693px; height: 1025px; background: var(--panel); }
  .portrait { position: absolute; background: linear-gradient(160deg, var(--photo-light), var(--photo-dark)); }
  .accent-bar { position: absolute; width: 7px; }
  .quote-mark {
    position: absolute; z-index: 0;
    font-family: "Montserrat", sans-serif; font-weight: 900;
    font-size: 380px; line-height: 380px; height: 200px; overflow: hidden;
    user-select: none;
  }
  .quote-text { position: absolute; z-index: 1; font-size: 12.6px; line-height: 16px; font-weight: 500; }
  .quote-text.spaced { letter-spacing: 1.2px; }
  .author { position: absolute; z-index: 1; font-size: 12.5px; font-weight: 700; text-align: right; white-space: nowrap; }
</style>
</head>
<body>
<div class="poster">
  <div class="frame"></div>
  <div class="panel"></div>

  <!-- Ned Pilsk -->
  <div class="accent-bar" style="left:120px;top:126px;height:158px;background:var(--teal-bar)"></div>
  <div class="portrait" style="left:127px;top:126px;width:144px;height:158px" role="img" aria-label="Black and white portrait of Ned Pilsk"></div>
  <span class="quote-mark" aria-hidden="true" style="left:292px;top:76px;color:var(--teal-mark)">&ldquo;</span>
  <p class="quote-text" style="left:329px;top:166px;width:373px">Success is nothing more than a few simple disciplines, practiced every day; while failure is simply a few errors in judgment, repeated every day. It is the accumulative weight of our disciplines and our judgments that leads us to either fortune or failure.</p>
  <p class="author" style="right:152px;top:242px;color:var(--teal-name)">Ned Pilsk</p>

  <!-- Ravindra Pallathuri -->
  <span class="quote-mark" aria-hidden="true" style="left:112px;top:232px;color:var(--salmon-mark)">&ldquo;</span>
  <p class="quote-text" style="left:148px;top:333px;width:385px">If we can really understand the problem, the answer will come out of it, because the answer is not separate from the problem.</p>
  <p class="author" style="right:325px;top:380px;color:var(--salmon-name)">Ravindra Pallathuri</p>
  <div class="portrait" style="left:581px;top:283px;width:143px;height:158px" role="img" aria-label="Black and white portrait of Ravindra Pallathuri"></div>
  <div class="accent-bar" style="left:724px;top:283px;height:158px;background:var(--salmon-bar)"></div>

  <!-- Tom Harlow -->
  <div class="accent-bar" style="left:120px;top:441px;height:157px;background:var(--mint-bar)"></div>
  <div class="portrait" style="left:130px;top:441px;width:140px;height:157px" role="img" aria-label="Colour portrait of Tom Harlow"></div>
  <span class="quote-mark" aria-hidden="true" style="left:278px;top:387px;color:var(--mint-mark)">&ldquo;</span>
  <p class="quote-text" style="left:323px;top:487px;width:390px">I tackle every big new problem by asking two questions:<br>&nbsp;&nbsp;Who has dealt with this problem well?<br>&nbsp;&nbsp;And what can we learn from them?</p>
  <p class="author" style="right:149px;top:534px;color:var(--mint-name)">Tom Harlow</p>

  <!-- Walt Brimsley -->
  <span class="quote-mark" aria-hidden="true" style="left:112px;top:549px;color:var(--lilac-mark)">&ldquo;</span>
  <p class="quote-text spaced" style="left:148px;top:660px;width:385px">Inaction breeds doubt and fear. Action breeds<br>confidence and courage.</p>
  <p class="author" style="right:324px;top:692px;color:var(--lilac-name)">Walt Brimsley</p>
  <div class="portrait" style="left:581px;top:600px;width:143px;height:155px" role="img" aria-label="Black and white portrait of Walt Brimsley"></div>
  <div class="accent-bar" style="left:724px;top:600px;height:155px;background:var(--lilac-bar)"></div>

  <!-- Harold Wexbury -->
  <div class="accent-bar" style="left:120px;top:758px;height:156px;background:var(--rose-bar)"></div>
  <div class="portrait" style="left:130px;top:758px;width:137px;height:156px" role="img" aria-label="Black and white portrait of Harold Wexbury"></div>
  <span class="quote-mark" aria-hidden="true" style="left:286px;top:706px;color:var(--rose-mark)">&ldquo;</span>
  <p class="quote-text" style="left:324px;top:789px;width:373px">What the pupil must learn, if he learns anything at all, is that the world will do most of the work for you, provided you cooperate with it by identifying how it really works and aligning with those realities. If we do not let the world teach us, it teaches us a lesson.</p>
  <p class="author" style="right:149px;top:868px;color:var(--rose-name)">Harold Wexbury</p>

  <!-- Lenny Druse -->
  <span class="quote-mark" aria-hidden="true" style="left:112px;top:865px;color:var(--salmon-mark)">&ldquo;</span>
  <p class="quote-text" style="left:148px;top:970px;width:385px">What's the one thing you can do, such that by doing it,<br>everything else will be easier or unnecessary?</p>
  <p class="author" style="right:324px;top:1002px;color:var(--salmon-name)">Lenny Druse</p>
  <div class="portrait" style="left:581px;top:914px;width:143px;height:158px" role="img" aria-label="Black and white portrait of Lenny Druse"></div>
  <div class="accent-bar" style="left:724px;top:914px;height:158px;background:var(--salmon-bar)"></div>
</div>
</body>
</html>
```